Gantry Moss Website Using Wordpress Jetpack CMS

Design a responsive SEO enabled website using Wordpress theme. 7 Pages with content to be developed. Primarily a single page site using Wordpress, so seeking a string website developer with capable skills in native understanding of SEO.

Unique Value Proposition
Sports Clubs are built on passion, people and facilities. All the volunteering and dedication in the world is limited by the level of quality services and benefits that are available to member. Access to funds and lack of knowledge create a void that holds back Club growth and access to improved facilities. Improved facilities draw members and discretionary spend to clubs, but Clubs are challenged in easily delivering expensive facility upgrades. We solve that problem in a way that's easy to digest and meets all the things considered and many that have not been considered at all!

High Level Concept
Gantry Moss seeks to solve a growing problem. How do clubs remain viable? How do clubs increase participation? How do clubs provide exceptional value for their members discretionary expenditure?

The heart of any solid sporting club is its people, volunteers all over the world, trying to make a difference.

Gantry Moss was built to facilitate Club growth by providing state of the art facilities without any capital exposure, in fact by providing a shared revenue model that allows for additional facilities to be layered on top of existing ones. Linking in an energy transfer scheme from the excess energy released in peak, the model allows extension to Club Member Energy Offers which exponentially grows revenues and provides strong fiscal opportunity back to the club.

At the centre of Gantry moss are Lights and Power which are a primary life blood of every club, particularly sports clubs offering training and coaching, like tennis, soccer, rugby lawn bowls, cricket and aussie rules to name a few

With energy bills reaching in excess of $10,000 per annum in many clubs, Gantry Moss aims to facilitate an energy performance contract for sports clubs that provides new facilities without financial exposure and a profit share on asset placement. This makes decision making easier for volunteer committees

Problems in Clubs
Membership and Participation
Attracting members and ensuring they get appropriate bang for buck takes time, energy and resources. Members seek quality environments with structured sport and easy access to sport facilities at times that suit.

Funding of Capital Assets
Clubs have considerable expenditure in infrastructure to ensure high quality facilities are upgraded and maintained.

Managing The Club
Clubs have considerable expenditure in day to day costs and unpaid volunteers are needed to maintain membership numbers and ensure high quality facilities and available.

The Solution
COST NEUTRAL INFRASTRUCTURE
Assess Power Expenditure
Identify Facilities Improvements - Value Adds etc
Provide Best Outcome Funding Model (Off Grid), Future Asset Returns, Booking/Club Mgnt
Deploy and Maintain Assets, Lower Maintenance

NEXT GEN ENERGY RETAIL SPONSORSHIP
Recover ZORN credits
Negotiate on Grid Sales
Develop Finance and Energy Rebates
Leverage Trading Mechanism

CLUB & MEMBER BENEFITS
Sponsor through Energy Purchase
Members Benefits in Offset Costs and Club Kickback
Giving Back drives the Club Improvement Plan and Income Generation + Carbon Neutral

Target Market(s)

Sports Clubs, Sports Club Committees, Local Councils looking to upgrade local club facilities

Coding

Coded - Design and coding required

Number of Pages Required

5+ page

Font styles to use
Sans Serif

Colors
acd036
848484

Requirements
Must have
• Responsive Design
• Must use Wordpress Jetpack for Delivery
• Target to use Theme with single page
• CMS for custom content additions
• Existing Domain
• Landing Pages
Nice to have
• https://www.quenmarix.com/en_AU/stillcore is an example of a site that displays characteristics
• Clean colour per logo and ability to expand easily using Wordpress
Should not have
• Hardcoded elements. CMS is a MUST HAVE

```html
<!DOCTYPE html>
<html lang="en">
<head>
<meta charset="utf-8">
<title>Gantry Moss – Lighting Up Sport</title>
<link rel="stylesheet" href="https://fonts.googleapis.com/css2?family=Raleway:wght@400;500;600;700;800&display=swap">
<style>
:root{
  --green:#8fc226;
  --green-dark:#78a81c;
  --ink:#1a1a1a;
  --grey:#848484;
  --white:#ffffff;
  --night:#161a1f;
}
*{margin:0;padding:0;box-sizing:border-box}
html,body{width:1200px;height:3114px;overflow:hidden;background:var(--white)}
body{position:relative;font-family:'Raleway',Arial,sans-serif;color:var(--ink)}
.abs{position:absolute}
.layer{position:absolute;left:0;top:0}

/* header */
.brand{left:92px;top:26px;color:var(--green);font-weight:800;font-size:28px;line-height:1;letter-spacing:.3px;white-space:nowrap;z-index:2}
.brand small{display:block;font-size:14px;font-weight:600;margin-top:4px;letter-spacing:0}
.nav{font-size:14px;color:var(--white)}
.nav a{color:var(--white);text-decoration:none;position:absolute;white-space:nowrap}
.nav a.active::after{content:"";position:absolute;left:0;right:0;bottom:-6px;height:2px;background:var(--white)}
.hero-title{left:0;width:1200px;top:266px;text-align:center;color:var(--white);font-weight:700;font-size:42px;letter-spacing:.5px}
.hero-tag{left:0;width:1200px;top:314px;text-align:center;color:var(--white);font-size:14px}
.btn{left:531px;top:349px;width:138px;height:34px;border-radius:17px;background:var(--green);color:var(--white);font-weight:700;font-size:13px;display:flex;align-items:center;justify-content:center;letter-spacing:.3px}

/* section headings */
.h2{font-weight:600;font-size:34px;color:var(--ink)}
.h2.light{color:var(--white)}

/* supply */
.supply{top:680px;width:330px;text-align:center}
.supply svg{display:block;margin:0 auto}
.supply h3{font-weight:500;font-size:23px;margin-top:38px}
.supply p{font-size:13px;line-height:22px;margin-top:18px;color:#333}

/* why */
.why-copy{left:131px;width:440px;font-size:13px;line-height:22px;color:var(--white)}
.why-photo{left:606px;top:1190px;width:498px;height:299px;box-shadow:0 14px 30px rgba(0,0,0,.35)}

/* testimonials */
.avatar{width:196px;height:196px;border-radius:50%;overflow:hidden}
.quote-mark{font-family:Georgia,serif;font-weight:700;font-size:78px;color:#333;line-height:1}
.t-name{left:349px;font-size:23px;color:var(--ink)}
.t-name b{color:var(--green);font-weight:600}
.t-body{left:349px;width:690px;font-size:13px;line-height:22px;color:#222}

/* how */
.how-title{left:0;width:1200px;top:2330px;text-align:center}

/* footer */
.foot-brand{left:112px;top:2712px;color:var(--green);font-weight:800;font-size:27px;line-height:1;white-space:nowrap;z-index:2}
.foot-brand small{display:block;font-size:14px;font-weight:600;margin-top:4px}
.foot-col{top:2841px;font-size:13px}
.foot-col h4{color:var(--green);font-weight:600;font-size:13px;margin-bottom:18px}
.foot-col li{list-style:none;line-height:28px;color:#222}
.social{display:flex;gap:14px;margin-top:4px}
.social span{width:20px;height:20px;border-radius:50%;background:var(--grey)}
.foot-rule{left:108px;top:3062px;width:976px;height:1px;background:#d6d6d6}
.copyright{left:0;width:1200px;top:3082px;text-align:center;font-size:12px;font-weight:600}
</style>
</head>
<body>

<!-- hero band and photo -->
<svg class="layer" width="1200" height="720" viewBox="0 0 1200 720" aria-hidden="true">
  <polygon points="0,490 470,505 580,645 1200,485 1200,510 452,697 452,522 0,512" fill="var(--green)"/>
</svg>
<svg class="layer" width="1200" height="720" viewBox="0 0 1200 720" role="img" aria-label="Night photo of two basketball players contesting the ball on an indoor court under bright arena lights">
  <defs>
    <radialGradient id="heroGlow" cx="0.55" cy="0.35" r="0.7">
      <stop offset="0" stop-color="#4a3a32"/>
      <stop offset="0.5" stop-color="#231c1a"/>
      <stop offset="1" stop-color="#0c0c10"/>
    </radialGradient>
  </defs>
  <polygon points="0,0 1200,0 1200,485 580,645 470,505 0,490" fill="url(#heroGlow)"/>
</svg>
<svg class="layer" width="1200" height="120" viewBox="0 0 1200 120" aria-hidden="true">
  <polygon points="640,0 1200,0 1200,62 640,110" fill="var(--green)"/>
</svg>

<div class="abs brand">GANTRY MOSS<small>Lighting Up Sport</small></div>
<nav class="abs nav" style="left:0;top:38px">
  <a class="active" href="#" style="left:702px">Home</a>
  <a href="#" style="left:773px">About Us</a>
  <a href="#" style="left:866px">Products</a>
  <a href="#" style="left:955px">Services</a>
  <a href="#" style="left:1042px">Contact Us</a>
</nav>
<h1 class="abs hero-title">GANTRY MOSS</h1>
<div class="abs hero-tag">Lighting Up Sport</div>
<div class="abs btn">BOOK ONLINE</div>

<!-- we supply -->
<h2 class="abs h2" style="left:187px;top:590px">We Supply</h2>

<div class="abs supply" style="left:101px;top:722px">
  <svg width="120" height="110" viewBox="0 0 120 110" fill="none" stroke="var(--green)" stroke-width="4" stroke-linejoin="round">
    <path d="M10 40 L60 20 L110 40 L60 60 Z"/><path d="M10 40 V80 L60 104 L110 80 V40"/><path d="M60 60 V104"/>
    <circle cx="60" cy="30" r="16"/><path d="M54 46 V54 H66 V46"/>
  </svg>
  <h3>Art Lights</h3>
  <p>Lorem ipsum dolor sit amet, consectetur adipiscing elit, sed do eiusmod tempor incididunt ut labore et dolore magna aliqua. Ut enim ad minim</p>
</div>
<div class="abs supply" style="left:433px;top:722px">
  <svg width="120" height="110" viewBox="0 0 120 110" fill="none" stroke="var(--green)" stroke-width="4" stroke-linejoin="round">
    <path d="M14 40 H96 L108 82 H4 Z"/><path d="M38 40 L32 82 M66 40 L70 82 M9 61 H103"/>
    <path d="M56 82 V100 M36 100 H76"/><circle cx="100" cy="18" r="9"/>
    <path d="M100 2 V5 M114 18 H117 M110 8 L112 6"/>
  </svg>
  <h3>Solar Technology</h3>
  <p>Lorem ipsum dolor sit amet, consectetur adipiscing elit, sed do eiusmod tempor incididunt ut labore et dolore magna aliqua. Ut enim ad minim</p>
</div>
<div class="abs supply" style="left:786px;top:722px">
  <svg width="120" height="110" viewBox="0 0 120 110" fill="none" stroke="var(--green)" stroke-width="4" stroke-linejoin="round">
    <rect x="10" y="24" width="100" height="76"/><rect x="20" y="12" width="16" height="12"/><rect x="84" y="12" width="16" height="12"/>
    <path d="M10 40 H110"/><path d="M64 50 L50 72 H64 L56 92 L76 64 H62 L70 50 Z"/>
  </svg>
  <h3>Battery Technolgy</h3>
  <p>Lorem ipsum dolor sit amet, consectetur adipiscing elit, sed do eiusmod tempor incididunt ut labore et dolore magna aliqua. Ut enim ad minim</p>
</div>

<!-- why choose us -->
<svg class="layer" width="1200" height="1700" viewBox="0 0 1200 1700" aria-hidden="true">
  <polygon points="0,1131 590,1131 590,1023 1200,1137 1200,1540 690,1540 690,1682 0,1526" fill="var(--green)"/>
</svg>
<h2 class="abs h2 light" style="left:131px;top:1205px">Why Choose Us?</h2>
<p class="abs why-copy" style="top:1278px">Lorem ipsum dolor sit amet, consectetur adipiscing elit, sed do eiusmod tempor incididunt ut labore et dolore magna aliqua. Ut enim ad minim veniam, quis nostrud exercitation ullamco laboris nisi ut aliquip ex ea commodo consequat. Duis aute irure dolor</p>
<p class="abs why-copy" style="top:1392px">Lorem ipsum dolor sit amet, consectetur adipiscing elit, sed do eiusmod tempor incididunt ut labore et dolore magna aliqua. Ut enim ad minim veniam, quis nostrud</p>
<svg class="abs why-photo" viewBox="0 0 498 299" role="img" aria-label="Photo of rows of solar panels in a grassy field under a bright sunlit sky">
  <defs>
    <linearGradient id="solarScene" x1="0" y1="0" x2="0" y2="1">
      <stop offset="0" stop-color="#2f6fc2"/><stop offset="0.45" stop-color="#9cc6ea"/>
      <stop offset="0.6" stop-color="#3b4c6a"/><stop offset="1" stop-color="#4f7a2a"/>
    </linearGradient>
  </defs>
  <rect width="498" height="299" fill="url(#solarScene)"/>
</svg>

<!-- testimonials -->
<h2 class="abs h2" style="left:722px;top:1590px">Testimonials</h2>

<svg class="abs avatar" style="left:124px;top:1694px" viewBox="0 0 196 196" role="img" aria-label="Portrait photo of a smiling man with short brown hair">
  <rect width="196" height="196" fill="#8a9a58"/>
</svg>
<div class="abs quote-mark" style="left:309px;top:1692px">&ldquo;</div>
<div class="abs t-name" style="top:1730px"><b>Tomas Ardell</b> , Newyork ,USA</div>
<p class="abs t-body" style="top:1777px">Lorem ipsum dolor sit amet, consectetur adipiscing elit, sed do eiusmod tempor incididunt ut labore et dolore magna aliqua. Ut enim ad minim veniam, quis nostrud exercitation ullamco laboris nisi ut aliquip ex ea commodo consequat Lorem ipsum dolor sit amet, consectetur adipiscing elit, sed do eiusmod tempor incididunt ut labore et dolore magna aliqua. Ut enim ad minim veniam, quis nostrud</p>

<svg class="abs avatar" style="left:124px;top:1929px" viewBox="0 0 196 196" role="img" aria-label="Portrait photo of a smiling bald man wearing glasses">
  <rect width="196" height="196" fill="#7f93a6"/>
</svg>
<div class="abs quote-mark" style="left:309px;top:1927px">&ldquo;</div>
<div class="abs t-name" style="top:1965px"><b>Tomas Ardell</b> , Newyork ,USA</div>
<p class="abs t-body" style="top:2012px">Lorem ipsum dolor sit amet, consectetur adipiscing elit, sed do eiusmod tempor incididunt ut labore et dolore magna aliqua. Ut enim ad minim veniam, quis nostrud exercitation ullamco laboris nisi ut aliquip ex ea commodo consequat Lorem ipsum dolor sit amet, consectetur adipiscing elit, sed do eiusmod tempor incididunt ut labore et dolore magna aliqua. Ut enim ad minim veniam, quis nostrud</p>

<!-- how it works -->
<svg class="layer" width="1200" height="2820" viewBox="0 0 1200 2820" aria-hidden="true">
  <polygon points="0,2238 623,2159 623,2190 0,2272" fill="var(--green)"/>
  <polygon points="632,2176 668,2176 662,2263 632,2263" fill="var(--green)"/>
</svg>
<svg class="layer" width="1200" height="2820" viewBox="0 0 1200 2820" role="img" aria-label="Dark photo of glowing vintage light bulbs hanging in a dim room">
  <defs>
    <radialGradient id="bulbGlow" cx="0.55" cy="0.5" r="0.6">
      <stop offset="0" stop-color="#4a3a2a"/><stop offset="0.6" stop-color="#22201c"/><stop offset="1" stop-color="#121315"/>
    </radialGradient>
  </defs>
  <polygon points="0,2272 623,2190 623,2263 1200,2263 1200,2655 345,2790 345,2672 0,2672" fill="url(#bulbGlow)"/>
</svg>
<svg class="layer" width="1200" height="2820" viewBox="0 0 1200 2820" aria-hidden="true">
  <polygon points="335,2684 1200,2655 1200,2700 345,2800" fill="var(--green)"/>
  <polygon points="0,2672 335,2672 345,2800 0,2800" fill="var(--white)"/>
</svg>
<h2 class="abs h2 light how-title">How It Works</h2>
<svg class="abs" style="left:557px;top:2424px" width="102" height="102" viewBox="0 0 102 102" aria-label="Play video">
  <circle cx="51" cy="51" r="47" fill="none" stroke="var(--green)" stroke-width="5"/>
  <polygon points="38,30 74,51 38,72" fill="var(--green)"/>
</svg>

<!-- footer -->
<div class="abs foot-brand">GANTRY MOSS<small>Lighting Up Sport</small></div>

<div class="abs foot-col" style="left:125px">
  <h4>Quick Links</h4>
  <ul><li>Home</li><li>About Us</li><li>Products</li><li>Services</li><li>Contact Us</li></ul>
</div>
<div class="abs foot-col" style="left:345px">
  <h4>Other Links</h4>
  <ul><li>Terms Of Use</li><li>Privacy Policy</li><li>Help</li></ul>
</div>
<div class="abs foot-col" style="left:579px">
  <h4>Services</h4>
  <ul><li>Art Lights</li><li>Solar Technology</li><li>Battery Technolgy</li></ul>
</div>
<div class="abs foot-col" style="left:853px">
  <h4>Connect With Us</h4>
  <div class="social"><span></span><span></span><span></span><span></span></div>
</div>

<div class="abs foot-rule"></div>
<div class="abs copyright">© 2018 Company Name &nbsp;|&nbsp; All Rights Reserved</div>

</body>
</html>
```